Lets get creative with Pelloway Finance Brochure

I have used artfolkhub before for a previous brochure which is attached business BRAMLE Automotive. I would like to work together on a new project PELLOWAY Finance. https://pellowayfinance.com.au/
It is a boutique Finance company ideally targeting the small to Medium business s along with consumer finance. I have attached previous brochure to give an idea of layout. Once we have a layout i will send wording through.

Target Market(s)

business owners

Industry/Entity Type

Finance

Font styles to use
Serif

Colors
0355a3
fef3ec

```html
<!DOCTYPE html>
<html lang="en">
<head>
<meta charset="utf-8">
<title>Pelloway Equipment – Trifold Brochure Concept 1</title>
<link rel="stylesheet" href="https://fonts.googleapis.com/css2?family=Lora:ital,wght@0,400;0,700;1,400&family=Playfair+Display:ital,wght@0,700;0,900;1,400&display=swap">
<style>
  :root {
    --blue: #0355a3;
    --navy: #0d2440;
    --cream: #fef3ec;
    --ink: #2a3440;
    --sky: #8fbde6;
    --page: #ffffff;
  }
  * { box-sizing: border-box; margin: 0; padding: 0; }
  html, body { width: 847px; height: 1200px; overflow: hidden; background: var(--page); }
  body { position: relative; font-family: "Lora", Georgia, serif; color: var(--ink); }

  .side-label {
    position: absolute; left: 87px;
    font-family: "Playfair Display", Georgia, serif; font-style: italic; font-weight: 400;
    font-size: 36px; color: var(--blue); line-height: 1;
  }
  .side-label.front { top: 14px; }
  .side-label.back { top: 610px; }

  .concept-rail { position: absolute; top: 0; left: 0; width: 847px; height: 1200px; pointer-events: none; }
  .concept-rail text { font-family: "Lora", Georgia, serif; font-size: 34px; fill: var(--blue); }

  .sheet {
    position: absolute; left: 87px; width: 688px; height: 532px;
    border: 2px solid var(--blue); overflow: hidden; background: var(--cream);
  }
  .sheet.front { top: 67px; }
  .sheet.back { top: 665px; }
  .sheet > svg.shapes { position: absolute; top: 0; left: 0; width: 684px; height: 528px; }

  .block { position: absolute; }
  .heading { font-family: "Playfair Display", Georgia, serif; font-weight: 900; font-size: 13.5px; line-height: 16.5px; color: var(--navy); white-space: nowrap; }
  .heading .accent { color: var(--blue); }
  .heading.on-colour { color: var(--cream); }
  .subhead { font-family: "Playfair Display", Georgia, serif; font-weight: 900; font-size: 10px; color: var(--navy); }
  .subhead.on-colour { color: var(--cream); }
  .copy { font-size: 8.6px; line-height: 12.5px; text-align: justify; width: 189px; color: var(--ink); }
  .copy.on-colour { color: var(--cream); }
  .copy p + p { margin-top: 10px; }
  .display { font-family: "Playfair Display", Georgia, serif; font-weight: 900; line-height: 1.12; white-space: nowrap; }

  .brand { position: absolute; text-align: center; font-family: "Lora", Georgia, serif; font-weight: 400; line-height: 1; }
  .brand .name { display: block; font-size: 12.5px; letter-spacing: 3.4px; }
  .brand .tag { display: block; font-size: 5px; letter-spacing: 3px; margin-top: 4px; }
  .brand.blue { color: var(--blue); }
  .brand.cream { color: var(--cream); }
  .brand.sky { color: var(--sky); }

  .feature-list { position: absolute; list-style: none; }
  .feature-list li { position: relative; font-size: 8.6px; line-height: 12.5px; }
  .quote-card {
    position: absolute; left: 25px; top: 239px; width: 192px; height: 153px;
    background: var(--cream); border-radius: 9px;
  }
  .quote-card .mark { position: absolute; left: 18px; top: 2px; font-family: "Playfair Display", Georgia, serif; font-size: 52px; font-weight: 900; color: var(--navy); }
  .quote-card blockquote { position: absolute; left: 16px; top: 48px; width: 164px; font-style: italic; font-size: 8px; line-height: 13.5px; text-align: justify; color: var(--ink); }
  .quote-card cite { position: absolute; right: 23px; top: 122px; font-style: normal; font-family: "Playfair Display", Georgia, serif; font-weight: 900; font-size: 10px; color: var(--navy); }

  .contact { position: absolute; left: 230px; top: 0; width: 228px; height: 528px; text-align: center; color: var(--cream); }
  .contact h3 { font-family: "Playfair Display", Georgia, serif; font-weight: 900; font-size: 14px; position: absolute; top: 350px; width: 100%; }
  .contact address { font-style: normal; font-size: 8.6px; line-height: 15px; position: absolute; top: 375px; width: 100%; }
  .contact address .gap { display: block; height: 14px; }

  .trifold-title { position: absolute; left: 472px; top: 366px; font-size: 17px; color: var(--cream); }
  .web { position: absolute; left: 472px; top: 494px; font-family: "Playfair Display", Georgia, serif; font-weight: 900; font-size: 10.5px; color: var(--sky); letter-spacing: 0.2px; }
  .hero-line { position: absolute; left: 25px; top: 110px; font-size: 21px; color: var(--cream); }
</style>
</head>
<body>

<div class="side-label front">front</div>
<div class="side-label back">Back</div>

<svg class="concept-rail" viewBox="0 0 847 1200" aria-hidden="true">
  <g>
    <text transform="translate(56 106) rotate(-90)" text-anchor="middle">1</text>
    <text transform="translate(56 333) rotate(-90)" text-anchor="middle">T</text>
    <text transform="translate(56 455) rotate(-90)" text-anchor="middle">P</text>
    <text transform="translate(56 577) rotate(-90)" text-anchor="middle">E</text>
    <text transform="translate(56 698) rotate(-90)" text-anchor="middle">C</text>
    <text transform="translate(56 828) rotate(-90)" text-anchor="middle">N</text>
    <text transform="translate(56 958) rotate(-90)" text-anchor="middle">O</text>
    <text transform="translate(56 1085) rotate(-90)" text-anchor="middle">C</text>
  </g>
  <g>
    <text transform="translate(829 106) rotate(-90)" text-anchor="middle">1</text>
    <text transform="translate(829 333) rotate(-90)" text-anchor="middle">T</text>
    <text transform="translate(829 455) rotate(-90)" text-anchor="middle">P</text>
    <text transform="translate(829 577) rotate(-90)" text-anchor="middle">E</text>
    <text transform="translate(829 698) rotate(-90)" text-anchor="middle">C</text>
    <text transform="translate(829 828) rotate(-90)" text-anchor="middle">N</text>
    <text transform="translate(829 958) rotate(-90)" text-anchor="middle">O</text>
    <text transform="translate(829 1085) rotate(-90)" text-anchor="middle">C</text>
  </g>
</svg>

<!-- FRONT SIDE -->
<section class="sheet front">
  <svg class="shapes" viewBox="0 0 684 528">
    <defs>
      <linearGradient id="cityTone" x1="0" y1="0" x2="0" y2="1">
        <stop offset="0" stop-color="#9aa3ab"/>
        <stop offset="0.55" stop-color="#6b655d"/>
        <stop offset="1" stop-color="#4a4640"/>
      </linearGradient>
      <linearGradient id="portraitTone" x1="0" y1="0" x2="1" y2="1">
        <stop offset="0" stop-color="#d6e4f2"/>
        <stop offset="1" stop-color="#3f6fa8"/>
      </linearGradient>
    </defs>
    <rect x="458" y="0" width="226" height="360" fill="url(#cityTone)" role="img" aria-label="Photo of a busy city street lined with tall buildings and yellow taxis"/>
    <polygon points="0,131 595,307 595,330 458,292 458,528 0,528" fill="var(--blue)"/>
    <polygon points="0,296 230,362 230,528 0,528" fill="var(--navy)"/>
    <polygon points="458,291 684,355 684,528 458,528" fill="var(--navy)"/>
    <circle cx="345" cy="248" r="58" fill="var(--blue)"/>
    <circle cx="345" cy="250" r="52" fill="url(#portraitTone)" role="img" aria-label="Portrait photo of a young professional"/>
    <g fill="var(--blue)">
      <circle cx="258" cy="59" r="13"/>
      <circle cx="258" cy="95" r="13"/>
      <circle cx="258" cy="136" r="13"/>
    </g>
    <g fill="none" stroke="var(--cream)" stroke-width="1.2" stroke-linecap="round">
      <circle cx="258" cy="57" r="4"/>
      <path d="M256.5 62 h3 M256.8 64 h2.4"/>
      <rect x="251.5" y="91" width="7" height="4" rx="2" transform="rotate(40 255 93)"/>
      <rect x="257.5" y="95" width="7" height="4" rx="2" transform="rotate(40 261 97)"/>
      <rect x="251" y="131" width="14" height="10" rx="1"/>
      <path d="M254 134 h4 M254 137 h4 M260 134 h3 M260 137 h3"/>
    </g>
    <g fill="var(--cream)">
      <circle cx="305" cy="475" r="4.5"/>
      <circle cx="336" cy="475" r="4.5"/>
      <circle cx="365" cy="475" r="4.5"/>
      <circle cx="394" cy="475" r="4.5"/>
    </g>
  </svg>

  <h2 class="block heading" style="left:26px; top:20px;"><span class="accent">LOREM IPSUM IS</span> SIMPLY<br>TEXT OF THE PRINTING .</h2>
  <div class="block copy" style="left:27px; top:63px;">Lorem Ipsum is simply dummy text of the printing and typesetting industry. Lorem Ipsum has been the industry's standard dummy text ever since the 1500s</div>

  <div class="brand blue" style="left:108px; top:137px; width:130px;">
    <span class="name">PELLOWAY</span><span class="tag">EQUIPMENT</span>
  </div>

  <h2 class="block heading on-colour" style="left:25px; top:194px;">SIMPLY TEXT OF THE<br>PRINTING</h2>

  <figure class="quote-card">
    <span class="mark">&ldquo;</span>
    <blockquote>Lorem Ipsum is simply dummy text of the printing and typesetting industry. Lorem Ipsum has been the industry's standard dummy text ever since the 1500s&rdquo;</blockquote>
    <cite>JOHN DOE</cite>
  </figure>

  <div class="block copy on-colour" style="left:27px; top:419px;">
    <p>Lorem Ipsum is simply dummy text of the printing and typesetting industry. Lorem Ipsum has been the industry's standard dummy text ever since the 1500s</p>
    <p>Lorem Ipsum is simply dummy text of the printing and typesetting industry. Lorem Ipsum has been the industry's standard</p>
  </div>

  <h3 class="block subhead" style="left:242px; top:20px;">WHY CHOOSE US</h3>
  <ul class="feature-list" style="left:284px; top:46px; width:160px;">
    <li>Lorem Ipsum is simply dummy text of the printing and typesetting</li>
    <li style="margin-top:13px;">Lorem Ipsum is simply dummy text of the printing and typesetting</li>
    <li style="margin-top:16px;">Lorem Ipsum is simply dummy text of the printing and typesetting industry.</li>
  </ul>

  <div class="contact">
    <h3>GET IN TOUCH</h3>
    <address>
      Company&nbsp; Group Corporation<br>
      48 Harbour Lane, Leeds, LS1 4QT
      <span class="gap"></span>
      Tel: 01632 960 418<br>
      Email: hello@pellowayfinance.com<br>
      Tel: 01632 960 418
    </address>
  </div>

  <div class="brand sky" style="left:462px; top:334px; width:120px;">
    <span class="name">PELLOWAY</span><span class="tag">EQUIPMENT</span>
  </div>
  <h1 class="trifold-title display">TRIFOLD BUSINESS<br>CREATIVE BROCHURE</h1>
  <div class="block copy on-colour" style="left:472px; top:430px; width:192px; font-size:8px; text-align:left;">Lorem Ipsum is simply dummy text of the printing and typesetting industry. Lorem Ipsum has been the industry's standard dummy text ever since the 1500s</div>
  <div class="web">WWW.PELLOWAYFINANCE.COM.AU</div>
</section>

<!-- BACK SIDE -->
<section class="sheet back">
  <svg class="shapes" viewBox="0 0 684 528">
    <defs>
      <linearGradient id="deskTone" x1="0" y1="0" x2="1" y2="1">
        <stop offset="0" stop-color="#3c4450"/>
        <stop offset="0.5" stop-color="#5c5f66"/>
        <stop offset="1" stop-color="#2a3039"/>
      </linearGradient>
      <linearGradient id="storeTone" x1="0" y1="0" x2="1" y2="1">
        <stop offset="0" stop-color="#d7dadd"/>
        <stop offset="1" stop-color="#7d8186"/>
      </linearGradient>
    </defs>
    <rect x="0" y="0" width="456" height="190" fill="url(#deskTone)" role="img" aria-label="Photo of people at a table working on tablets"/>
    <polygon points="230,156 456,85 456,528 230,528" fill="var(--blue)"/>
    <rect x="456" y="159" width="228" height="133" fill="url(#storeTone)" role="img" aria-label="Photo of a smiling customer being served in a store"/>
    <rect x="456" y="291" width="228" height="237" fill="var(--navy)"/>
    <g fill="var(--cream)" stroke="var(--sky)" stroke-width="1.5">
      <circle cx="259" cy="333" r="12"/>
      <circle cx="259" cy="371" r="12"/>
      <circle cx="259" cy="408" r="12"/>
      <circle cx="259" cy="445" r="12"/>
      <circle cx="259" cy="484" r="12"/>
    </g>
    <g fill="none" stroke="var(--navy)" stroke-width="1.2" stroke-linecap="round">
      <circle cx="259" cy="331" r="3.5"/>
      <path d="M257.5 336 h3"/>
      <path d="M254 369 h3 l6 -4 v11 l-6 -4 h-3 z"/>
      <path d="M253 410 a6 6 0 0 1 12 0 z"/>
      <rect x="253" y="442" width="12" height="6" rx="3"/>
      <rect x="253" y="479" width="12" height="9"/>
    </g>
    <g fill="none" stroke="var(--cream)" stroke-width="1.3" stroke-linecap="round" stroke-linejoin="round">
      <circle cx="479" cy="379" r="6"/><path d="M476 379 l2 2 l4 -4"/>
      <circle cx="479" cy="416" r="6"/><path d="M476 416 l2 2 l4 -4"/>
      <circle cx="479" cy="453" r="6"/><path d="M476 453 l2 2 l4 -4"/>
      <circle cx="479" cy="490" r="6"/><path d="M476 490 l2 2 l4 -4"/>
    </g>
  </svg>

  <h1 class="hero-line display">WE MAKE SOME<br>MORE INNOVATIVE</h1>

  <h3 class="block subhead" style="left:25px; top:218px;">WHY CHOOSE US</h3>
  <div class="block copy" style="left:25px; top:243px; width:192px;">
    <p>Lorem Ipsum is simply dummy text of the printing and typesetting industry. Lorem Ipsum has been the industry's standard dummy text ever since the 1500s.</p>
    <p>Lorem Ipsum is simply dummy text of the printing and typesetting industry. Lorem Ipsum has been the industry's standard dummy text ever since.</p>
    <p>1500sLorem Ipsum is simply dummy text of the printing and typesetting industry. Lorem Ipsum has been the industry's standard dummy.</p>
    <p>.text ever since the 1500sLorem Ipsum is simply dummy text of the printing and typesetting industry. Lorem Ipsum has been the industry's standard dummy text ever since the 1500s.</p>
  </div>

  <div class="brand cream" style="left:330px; top:134px; width:130px;">
    <span class="name">PELLOWAY</span><span class="tag">EQUIPMENT</span>
  </div>
  <h2 class="block heading on-colour" style="left:242px; top:175px;">LOREM IPSUM IS SIMPLY<br>TEXT OF THE PRINTING .</h2>
  <div class="block copy on-colour" style="left:245px; top:218px;">Lorem Ipsum is simply dummy text of the printing and typesetting industry. Lorem Ipsum has been the industry's standard dummy text.</div>
  <h3 class="block subhead on-colour" style="left:242px; top:290px;">WHY CHOOSE US</h3>
  <ul class="feature-list" style="left:285px; top:324px; width:170px; color:var(--cream);">
    <li>Lorem Ipsum is simply dummy text of the printing and typesetting industry.</li>
    <li style="margin-top:12.5px;">Lorem Ipsum is simply dummy text of the printing and typesetting industry.</li>
    <li style="margin-top:12.5px;">Lorem Ipsum is simply dummy text of the printing and typesetting industry.</li>
    <li style="margin-top:12.5px;">Lorem Ipsum is simply dummy text of the printing and typesetting industry.</li>
    <li style="margin-top:12.5px;">Lorem Ipsum is simply dummy text of the printing and typesetting industry.</li>
  </ul>

  <h3 class="block subhead" style="left:472px; top:22px;">WHAT WE DO?</h3>
  <div class="block copy" style="left:472px; top:43px;">Lorem Ipsum is simply dummy text of the printing and typesetting industry. Lorem Ipsum has been the industry's standard dummy text ever since the 1500sLorem Ipsum is simply dummy text of the printing and typesetting industry. Lorem Ipsum has been the industry's standard dummy text ever since the 1500s</div>

  <h2 class="block heading on-colour" style="left:472px; top:314px;">LOREM IPSUM IS SIMPLY<br>TEXT OF THE PRINTING .</h2>
  <ul class="feature-list" style="left:495px; top:373px; width:170px; color:var(--cream);">
    <li>Lorem Ipsum is simply dummy text of the printing and typesetting industry.</li>
    <li style="margin-top:12px;">Lorem Ipsum is simply dummy text of the printing and typesetting industry.</li>
    <li style="margin-top:12px;">Lorem Ipsum is simply dummy text of the printing and typesetting industry.</li>
    <li style="margin-top:12px;">Lorem Ipsum is simply dummy text of the printing and typesetting industry.</li>
  </ul>
</section>

</body>
</html>
```